KB Sports & Remedial Massage needs a new logo & business card design

The design is for my Sports and remedial massage business. My business is aimed at everyone who has a muscle ache or injury so not just sports related. I need a design which is sharp, clear and professional. No greens, or pastel colours or floral/girly designs. Perhaps just a Navy background and white text or other way around or perhaps grey. I want to make it clear that I treat everyone and not just sporty people.

Target Market(s)

People with muscle aches or sports injuries

Industry/Entity Type

Health And Wellness

Contact Information for Business Card

It needs to also include the following:
Name: Megan Hartwell
Mobile No: 07493 215 648
Email: meganhartwell@parcelnet.example
Qualifications: Dip SM, Dip SRM

Logo Text

KB Sports & Remedial Massage

Font styles to use
Serif
Other font styles liked:
• Tahoma, Verdana

Colors
5c5c5c
7f7f7f
9d9d9d
0255a3
3176b5
85abd2

Requirements
Must have
• I was thinking of a few simple people figures at the bottom of the card to highlight this i.e. a gardener, musician mixed in with a cyclist and tennis player.
Should not have
• Anything which indicates beauty therapy or relaxing. I am there to get rid of aches and pains and often to give rehab to certain injuries.

```html
<!DOCTYPE html>
<html lang="en">
<head>
<meta charset="utf-8">
<title>KB Sports &amp; Remedial Massage – Business Card</title>
<link rel="stylesheet" href="https://fonts.googleapis.com/css2?family=Noto+Sans:wght@400;600;700&display=swap">
<style>
  :root {
    --card-black: #000000;
    --card-blue: #0255a3;
    --text-white: #ffffff;
    --figure-tone: #e4e4e4;
    --page-bg: #d6d6d6;
    --font-main: "Noto Sans", Tahoma, Verdana, sans-serif;
  }
  * { box-sizing: border-box; margin: 0; padding: 0; }
  html, body {
    width: 992px; height: 1200px; overflow: hidden;
    background: var(--page-bg);
    font-family: var(--font-main);
  }
  .business-card {
    position: absolute;
    left: 98px;
    width: 808px; height: 462px;
    border-radius: 20px;
    overflow: hidden;
    background: var(--card-black);
    color: var(--text-white);
  }
  .business-card--first { top: 103px; }
  .business-card--second { top: 624px; }
  .card-wave { position: absolute; inset: 0; width: 100%; height: 100%; }
  .business-name {
    position: absolute; top: 40px; left: 0; width: 100%;
    text-align: center; font-size: 40px; font-weight: 400; letter-spacing: 0.2px;
  }
  .client-figures {
    position: absolute; left: 132px; top: 125px; width: 550px; height: 153px;
    border-radius: 10px;
    background: linear-gradient(180deg, var(--figure-tone), #bfbfbf);
    opacity: 0.9;
  }
  .practitioner-name {
    position: absolute; left: 75px; top: 344px;
    font-size: 34px; font-weight: 400;
  }
  .qualifications {
    position: absolute; left: 75px; top: 395px;
    font-size: 18px; font-weight: 600;
  }
  .contact-divider {
    position: absolute; left: 374px; top: 354px;
    width: 2px; height: 72px; background: var(--text-white);
  }
  .contact-list { position: absolute; left: 425px; top: 362px; list-style: none; }
  .contact-item {
    display: flex; align-items: center; gap: 16px;
    font-size: 19px; height: 24px; margin-bottom: 11px;
  }
  .contact-icon { width: 17px; height: 17px; flex: none; }
</style>
</head>
<body>

<article class="business-card business-card--first">
  <svg class="card-wave" viewBox="0 0 808 462" aria-hidden="true">
    <path d="M0 237 Q404 420 808 232 L808 462 L0 462 Z" fill="var(--card-blue)"/>
  </svg>
  <h1 class="business-name">KB Sports &amp; Remedial Massage</h1>
  <div class="client-figures" role="img" aria-label="White silhouettes of a tennis player, a cyclist, a gardener with a watering can and a saxophone player"></div>
  <p class="practitioner-name">Megan Hartwell</p>
  <p class="qualifications">Dip SM, Dip SRM</p>
  <span class="contact-divider"></span>
  <ul class="contact-list">
    <li class="contact-item">
      <svg class="contact-icon" viewBox="0 0 16 16" aria-hidden="true"><rect width="16" height="16" rx="2" fill="#fff"/><path d="M4 5.5h8v1.5h-2v-1h-4v1h-2z M5 8h6l1 4h-8z" fill="var(--card-blue)"/></svg>
      <span>07493 215 648</span>
    </li>
    <li class="contact-item">
      <svg class="contact-icon" viewBox="0 0 16 16" aria-hidden="true"><rect width="16" height="16" rx="2" fill="#fff"/><path d="M5 3l2 2.5-1.2 1.2c.6 1.4 1.7 2.5 3.1 3.1L10.1 8.6 12.6 10.6 11.2 13C7.4 12.6 3.6 8.8 3.2 5z" fill="var(--card-blue)"/></svg>
      <span>meganhartwell@parcelnet.example</span>
    </li>
  </ul>
</article>

<article class="business-card business-card--second">
  <svg class="card-wave" viewBox="0 0 808 462" aria-hidden="true">
    <path d="M0 237 Q404 420 808 232 L808 462 L0 462 Z" fill="var(--card-blue)"/>
  </svg>
  <h2 class="business-name">KB Sports &amp; Remedial Massage</h2>
  <div class="client-figures" role="img" aria-label="White silhouettes of a tennis player, a cyclist, a gardener with a watering can and a saxophone player"></div>
  <p class="practitioner-name">Megan Hartwell</p>
  <p class="qualifications">Dip SM, Dip SRM</p>
  <span class="contact-divider"></span>
  <ul class="contact-list">
    <li class="contact-item">
      <svg class="contact-icon" viewBox="0 0 16 16" aria-hidden="true"><rect width="16" height="16" rx="2" fill="#fff"/><path d="M4 5.5h8v1.5h-2v-1h-4v1h-2z M5 8h6l1 4h-8z" fill="var(--card-blue)"/></svg>
      <span>07493 215 648</span>
    </li>
    <li class="contact-item">
      <svg class="contact-icon" viewBox="0 0 16 16" aria-hidden="true"><rect width="16" height="16" rx="2" fill="#fff"/><path d="M5 3l2 2.5-1.2 1.2c.6 1.4 1.7 2.5 3.1 3.1L10.1 8.6 12.6 10.6 11.2 13C7.4 12.6 3.6 8.8 3.2 5z" fill="var(--card-blue)"/></svg>
      <span>meganhartwell@parcelnet.example</span>
    </li>
  </ul>
</article>

</body>
</html>
```